Home Health Company Needs a Corporate Identity Package

We need a corporate identity package (see what it should include below) for a home health care company. The design should be professional, uncluttered, simple and created in Publisher (so that we can edit the design in the future, if necessary. )
We need the following created:
-Presentation folder
-Business card template (color, double sided)
-Letterhead
-Stationary
-postcard sized marketing piece (5.5" x 8.5", color, double sided)

Target Market(s)

We are in the business of supplying personal care aids for in home care. Our services are directed towards older, retired individuals with some disability or illness. However, we will be marketing to the children or relatives of our in home clients. We want our logo to emphasize our reliability and personalized services.

Industry/Entity Type

Home Health Care

Requirements
Must have
• The design should be professional, uncluttered, simple and created in Publisher (so that we can edit the design in the future, if necessary. )

```html
<!DOCTYPE html>
<html lang="en">
<head>
<meta charset="utf-8">
<title>Willow Home Health – Letterhead</title>
<link rel="stylesheet" href="https://fonts.googleapis.com/css2?family=Open+Sans:wght@400;600;700&display=swap">
<style>
  :root {
    --backdrop: #ececec;
    --paper: #ffffff;
    --brand-blue: #5cc3ee;
    --rule-grey: #5a5d61;
    --footer-text: #ffffff;
  }
  html, body {
    margin: 0;
    padding: 0;
    width: 1200px;
    height: 936px;
    overflow: hidden;
    background: var(--backdrop);
    font-family: "Open Sans", Arial, sans-serif;
  }
  .letterhead {
    position: absolute;
    left: 300px;
    top: 70px;
    width: 600px;
    height: 796px;
    background: var(--paper);
    box-shadow: 0 6px 18px rgba(0, 0, 0, 0.12);
    display: flex;
    flex-direction: column;
  }
  .letterhead__header {
    padding: 44px 0 0 52px;
  }
  .brand-name {
    margin: 0;
    font-weight: 700;
    font-size: 30px;
    line-height: 1.05;
    color: var(--brand-blue);
    letter-spacing: -0.3px;
    width: 200px;
  }
  .letterhead__body {
    flex: 1;
  }
  .letterhead__footer {
    border-top: 3px solid var(--rule-grey);
    background: var(--brand-blue);
    height: 58px;
    display: flex;
    align-items: center;
    padding: 0 26px;
    color: var(--footer-text);
    font-size: 10px;
    line-height: 1.35;
  }
  .footer-brand {
    font-weight: 600;
    font-size: 10px;
    width: 70px;
  }
  .footer-block {
    flex: 1;
    padding-left: 14px;
  }
  .footer-divider {
    width: 1px;
    height: 20px;
    background: var(--footer-text);
    margin: 0 18px;
  }
</style>
</head>
<body>
  <main class="letterhead">
    <header class="letterhead__header">
      <h1 class="brand-name">Willow Home Health</h1>
    </header>
    <section class="letterhead__body"></section>
    <footer class="letterhead__footer">
      <div class="footer-brand">Willow</div>
      <div class="footer-block footer-address">street name, city name,<br>state zip code</div>
      <span class="footer-divider"></span>
      <div class="footer-block footer-phone">Phone: 555-555-5555<br>Fax: 555-555-5555</div>
      <span class="footer-divider"></span>
      <div class="footer-block footer-web">info@website.com<br>www.website.com</div>
    </footer>
  </main>
</body>
</html>
```